Pier Grove Profile Bacground Needed

I need a simple Pier Grove Background graphic for my Pier Grove profile. My website is www.MeridelVKP.com
I have attached a couple of photos and our logo.

The tag line is: BEAUTY | FUNCTION | ON TIME | ON BUDGET

```html
<!DOCTYPE html>
<html lang="en">
<head>
<meta charset="utf-8">
<title>Meridel – Pier Grove Profile Background</title>
<link href="https://fonts.googleapis.com/css2?family=Montserrat:wght@500;600;700&display=swap" rel="stylesheet">
<style>
  :root {
    --page: #e4e4e2;
    --banner: #efefef;
    --ink: #0d0d0d;
    --paper: #ffffff;
    --rule: #6f6f6f;
    --arrow: #c4c4c4;
    --photo-light: #d9d6d0;
    --photo-mid: #a9a49b;
    --photo-dark: #3a3c3d;
  }
  * { margin: 0; padding: 0; box-sizing: border-box; }
  html, body { width: 1200px; height: 800px; overflow: hidden; }
  body {
    background: var(--page);
    font-family: "Montserrat", sans-serif;
    position: relative;
  }
  .banner {
    position: absolute;
    left: 0; top: 250px;
    width: 1200px; height: 301px;
    background: var(--banner);
    overflow: hidden;
  }
  .side-block {
    position: absolute; left: 0; top: 0;
    width: 212px; height: 301px;
    background: var(--ink);
  }
  .social-list {
    position: absolute; left: 28px; top: 73px;
    display: flex; flex-direction: column; gap: 12px;
  }
  .social-list span {
    display: block; width: 30px; height: 30px;
    border-radius: 7px; background: var(--paper);
  }
  .photo-frame {
    position: absolute; left: 92px; top: 34px;
    width: 637px; height: 232px;
    background: var(--paper);
  }
  .photo {
    position: absolute; left: 9px; top: 8px;
    width: 619px; height: 217px;
    background: linear-gradient(180deg, var(--photo-light) 0%, var(--photo-mid) 55%, var(--photo-dark) 78%, var(--photo-mid) 100%);
  }
  .outline-frame { position: absolute; left: 0; top: 0; }
  .website {
    position: absolute; left: 336px; top: 273px;
    width: 188px;
    font-size: 14px; font-weight: 600; letter-spacing: 1.4px;
    color: var(--ink); text-align: center;
  }
  .arrows { position: absolute; left: 805px; top: 33px; }
  .brand {
    position: absolute; left: 1074px; top: 26px;
    display: flex; align-items: center; gap: 6px;
    font-size: 19px; font-weight: 600; color: var(--ink); letter-spacing: 0.5px;
  }
  .brand-mark { width: 10px; height: 10px; background: var(--ink); }
  .tagline-top, .tagline-band, .tagline-bottom {
    position: absolute; left: 729px; width: 471px; text-align: center; color: var(--ink);
  }
  .tagline-top {
    top: 72px; font-size: 44px; font-weight: 600; letter-spacing: 1px;
  }
  .tagline-band {
    top: 126px; height: 66px; background: var(--ink); color: var(--paper);
    font-size: 58px; font-weight: 600; line-height: 66px; letter-spacing: 1px;
  }
  .tagline-bottom {
    top: 201px; font-size: 22px; font-weight: 600; letter-spacing: 0.5px;
  }
</style>
</head>
<body>
  <section class="banner">
    <div class="side-block"></div>
    <div class="social-list" aria-label="Social links">
      <span></span><span></span><span></span><span></span>
    </div>
    <div class="photo-frame">
      <div class="photo" role="img" aria-label="Photo of a bright kitchen with grey cabinets, marble backsplash and a dark island with brass stools"></div>
    </div>
    <svg class="outline-frame" width="1200" height="301" viewBox="0 0 1200 301">
      <polyline points="336,17 745,17 745,284 526,284" fill="none" stroke="var(--rule)" stroke-width="2.5"/>
    </svg>
    <p class="website">www.MeridelVKP.com</p>
    <svg class="arrows" width="54" height="12" viewBox="0 0 54 12">
      <polygon points="0,0 10,6 0,12" fill="var(--arrow)"/>
      <polygon points="11,0 21,6 11,12" fill="var(--arrow)"/>
      <polygon points="22,0 32,6 22,12" fill="var(--arrow)"/>
      <polygon points="33,0 43,6 33,12" fill="var(--arrow)"/>
      <polygon points="44,0 54,6 44,12" fill="var(--arrow)"/>
    </svg>
    <div class="brand"><span class="brand-mark"></span>MERIDEL</div>
    <h1 class="tagline-top">BEAUTY</h1>
    <h2 class="tagline-band">FUNCTION</h2>
    <p class="tagline-bottom">ON TIME | ON BUDGET</p>
  </section>
</body>
</html>
```